TWIG - Tiny Wild Infusion Garden - Craft Cocktails Mixes.

and we want to sell craft cocktails mixes (dried ingredients) in jars. The person buying them would add the alcohol.

LOGO TO BE WHITE ON WEBSITE

We are doing something similar to this, but would like to make them better... with better names and better mixers.

Here are some competing sites.

https://www.fernhollowmixers.com

https://pennyspours.com

In terms of style, I love this layout and look of a website:

https://www.rvdunespirits.com/

Or this

https://www.stitchthevale.com/

Target Market(s)

Target market is 21-50. Anyone who wants to throw a party or make amazing cocktails, but doesn't have the full bar to do so. It's just pour... wait 3 days. Strain. Mix with soda, tonic, fruit juice, kombucha over ice and drink.

Coding

Coded - Design and coding required

Number of Pages Required

5+ page

Other font styles liked:
• LOGO TO BE WHITE ON WEBSITE - Match the font of the Logo

Colors
00AB8E
00BBA5
67D7C9
C6EFE9
E9F9F6

Requirements
Must have
• Point of sale. The ability to add photos and videos with ease
Nice to have
• Great photography. Teal background tabs with white logo.

```html
<!DOCTYPE html>
<html lang="en">
<head>
<meta charset="utf-8">
<title>TWIG Craft Cocktails</title>
<link rel="stylesheet" href="https://fonts.googleapis.com/css2?family=Bebas+Neue&family=Roboto:wght@400;500;700&family=Lato:wght@400;700&display=swap">
<style>
:root{
  --teal:#00AB8E;
  --teal-bright:#00BBA5;
  --teal-soft:#67D7C9;
  --teal-pale:#C6EFE9;
  --teal-mist:#E9F9F6;
  --ink:#1F1F1F;
  --text:#333333;
  --white:#FFFFFF;
}
*{box-sizing:border-box;margin:0;padding:0}
html,body{width:1200px;height:3841px;overflow:hidden}
body{position:relative;background:var(--white);font-family:"Roboto",sans-serif;color:var(--text)}
.abs{position:absolute}
.display{font-family:"Bebas Neue",sans-serif;color:var(--ink);letter-spacing:.5px;line-height:1.1}
.copy{font-family:"Lato",sans-serif;font-size:15.5px;line-height:25.8px;color:var(--text)}
.btn-outline{position:absolute;border:2.5px solid var(--teal);border-radius:30px;font:500 14.5px "Roboto",sans-serif;color:var(--ink);display:flex;align-items:center;justify-content:center;letter-spacing:.3px;background:var(--white)}

/* top bar + nav */
.topbar{left:0;top:0;width:1200px;height:28px;background:var(--teal);color:var(--white);font-size:14px}
.topbar .mail{left:110px;top:5px;display:flex;gap:9px;align-items:center}
.topbar .promo{left:0;width:1200px;top:5px;text-align:center}
.topbar .tools{right:108px;top:4px;display:flex;gap:26px}
.nav{left:0;top:28px;width:1200px;height:57px;background:var(--white);font-size:15px;color:#444}
.nav a{position:absolute;top:19px;text-decoration:none;color:#444}
.nav .shop-pill{top:13px;left:995px;width:95px;height:33px;border:2.5px solid var(--teal);border-radius:20px;display:flex;align-items:center;justify-content:center;font-weight:500;color:var(--ink)}
.brand-disc{left:537px;top:28px;width:126px;height:92px;background:var(--teal);border-radius:0 0 63px 63px;z-index:5;display:flex;align-items:center;justify-content:center;font:700 30px "Roboto",sans-serif;color:var(--white);letter-spacing:3px}

/* hero */
.hero{left:0;top:85px;width:1200px;height:670px}
.hero h1{right:112px;top:185px;font-size:60px;text-align:right;line-height:1.05}
.hero .tag{right:112px;top:326px;font:700 19px "Roboto",sans-serif;color:var(--ink);letter-spacing:.5px}
.hero .btn-outline{left:914px;top:380px;width:174px;height:47px;background:transparent}

/* intro */
.intro h2{left:112px;top:870px;font-size:35px}
.intro .copy{left:112px;top:974px;width:450px}
.ring{position:absolute;border-radius:50%}
.badge{position:absolute;border-radius:50%;border:4px solid var(--white);display:flex;align-items:center;justify-content:center;color:var(--white)}

/* collection */
.collection{left:0;top:1322px;width:1200px;height:578px;background:var(--teal)}
.collection h2{width:1200px;top:48px;text-align:center;color:var(--white);font-size:38px}
.card{position:absolute;top:131px;width:235px;height:350px;background:var(--white);text-align:center}
.card .shot{height:194px}
.card .stars{margin-top:14px;font-size:15px;color:var(--ink)}
.card .stars b{color:var(--teal);letter-spacing:1px;font-weight:400}
.card .name{margin-top:8px;font-size:15px;color:var(--ink)}
.card .price{margin-top:10px;font-size:15px;color:var(--ink);font-weight:500}
.card .price s{color:#777;font-weight:400;margin-left:8px}
.card .add{margin:12px auto 0;width:98px;height:30px;border-radius:16px;background:var(--teal-bright);color:var(--white);font-size:14px;display:flex;align-items:center;justify-content:center}
.dots{top:528px;left:570px;display:flex;gap:8px}
.dots i{width:12px;height:12px;border-radius:50%;background:var(--white)}

/* recipes */
.recipes h2{left:632px;top:2032px;font-size:35px}
.recipes .copy{left:632px;top:2093px;width:450px}

/* spirits */
.spirits{left:0;top:2469px;width:1200px;height:329px;background:var(--teal-mist)}
.spirits h2{width:1200px;top:56px;text-align:center;font-size:35px}
.spirit{position:absolute;top:124px;width:150px;height:146px;text-align:center}
.spirit.is-active{background:var(--white);box-shadow:0 2px 10px rgba(0,0,0,.12)}
.spirit svg{margin-top:12px}
.spirit span{position:absolute;left:0;width:150px;top:106px;font:22px "Bebas Neue",sans-serif;color:var(--ink)}

/* choose */
.choose h2{left:115px;top:2930px;font-size:35px}
.choose .copy{left:115px;top:2991px;width:450px}

/* footer */
.footer{left:0;top:3326px;width:1200px;height:515px;background:var(--teal);color:var(--white)}
.footer h3{font:32px "Bebas Neue",sans-serif;color:var(--white);letter-spacing:.5px}
.signup{left:562px;top:52px;width:488px;height:50px;background:var(--white);border-radius:26px}
.signup span{position:absolute;left:30px;top:15px;font-size:14.5px;color:#444}
.signup b{position:absolute;right:3px;top:3px;width:122px;height:44px;border-radius:22px;background:var(--teal-bright);color:var(--white);font-weight:500;font-size:14.5px;display:flex;align-items:center;justify-content:center}
.rule{left:112px;width:976px;height:1px;background:rgba(255,255,255,.55)}
.col h4{font:23px "Bebas Neue",sans-serif;letter-spacing:.4px;margin-bottom:11px}
.col li{list-style:none;font-size:15px;line-height:25.5px}
.contact-row{display:flex;gap:14px;font-size:14.5px;line-height:21px;margin-bottom:20px}
.socials{display:flex;gap:20px}
.socials i{width:18px;height:18px;background:var(--white);border-radius:3px}
.copyright{left:0;width:1200px;top:457px;text-align:center;font-size:14.5px}
</style>
</head>
<body>

<!-- top bar -->
<div class="abs topbar">
  <div class="abs mail">
    <svg width="20" height="14" viewBox="0 0 20 14"><rect x="1" y="1" width="18" height="12" fill="none" stroke="#fff" stroke-width="1.6"/><path d="M1 1l9 7 9-7" fill="none" stroke="#fff" stroke-width="1.6"/></svg>
    <span>Info@TWIG.com</span>
  </div>
  <div class="abs promo">Free shipping on all orders over 75$</div>
  <div class="abs tools">
    <svg width="18" height="18" viewBox="0 0 18 18"><circle cx="9" cy="5" r="4" fill="#fff"/><path d="M1 18c0-5 3.5-7 8-7s8 2 8 7z" fill="#fff"/></svg>
    <svg width="20" height="18" viewBox="0 0 20 18"><path d="M0 1h4l3 10h10l2-7H6" fill="none" stroke="#fff" stroke-width="2"/><circle cx="8" cy="15" r="2" fill="#fff"/><circle cx="16" cy="15" r="2" fill="#fff"/></svg>
  </div>
</div>

<nav class="abs nav">
  <a style="left:228px">ABOUT US</a>
  <a style="left:330px">SHOP</a>
  <a style="left:400px">GIFTS</a>
  <a style="left:725px">RECIPES</a>
  <a style="left:816px">MERCH</a>
  <a style="left:897px">STOCKISTS</a>
  <a class="shop-pill">SHOP</a>
</nav>
<div class="abs brand-disc">TWIG</div>

<!-- hero -->
<section class="abs hero">
  <svg class="abs" style="left:0;top:0" width="1200" height="670" viewBox="0 0 1200 670">
    <defs>
      <linearGradient id="heroTone" x1="0" y1="0" x2="1" y2="1">
        <stop offset="0" stop-color="#7FA36B"/>
        <stop offset=".45" stop-color="#B9D8E4"/>
        <stop offset=".75" stop-color="#E9E6DC"/>
        <stop offset="1" stop-color="#6E8A52"/>
      </linearGradient>
    </defs>
    <path d="M0 0H1200V570C1080 560 980 610 850 640C720 670 620 640 470 610C330 585 200 575 90 600C50 610 20 605 0 610Z" fill="url(#heroTone)" role="img" aria-label="Photo of a mojito with lime and mint on a beach bar"/>
    <path d="M0 612C60 600 120 580 220 585C330 590 420 620 520 640C620 660 720 670 840 645C960 620 1080 575 1200 570" fill="none" stroke="#00AB8E" stroke-width="6"/>
    <path d="M1133 486v40M1124 516l9 12 9-12" fill="none" stroke="#111" stroke-width="2.4"/>
  </svg>
  <h1 class="abs display">WELCOME TO THE TWIG<br>CRAFT COCKTAILS</h1>
  <div class="abs tag">APERIAM, EAQUE IPSA QUAE AB</div>
  <div class="btn-outline">GET STARTED</div>
</section>

<!-- intro -->
<section class="intro">
  <h2 class="abs display">BUILDING COCKTAIL<br>CONFIDENCE EVERYWHERE</h2>
  <p class="abs copy">Eaque Ipsa Quae Ab Illo Inventore Veritatis Et Quasi Architecto Beatae Vitae Dicta Sunt Explicabo. Nemo Enim Ipsam Voluptatem Quia Voluptas Sit Aspernatur Aut Odit Aut Fugit, Sed Quia Consequuntur Magni Dolores Eos Qui Ratione Voluptatem Sequi Nesciunt. Neque Porro Quisquam Est, Qui Dolorem Ipsum Quia Dolor Sit Amet, Consectetur, Adipisci Velit, Sed Quia Non</p>
  <div class="btn-outline" style="left:112px;top:1154px;width:154px;height:45px">LEARN MORE</div>
  <div class="ring" style="left:641px;top:830px;width:420px;height:420px;background:var(--teal-pale)"></div>
  <div class="ring" style="left:655px;top:844px;width:392px;height:392px;background:var(--teal)"></div>
  <div class="ring" style="left:675px;top:864px;width:354px;height:354px;background:linear-gradient(160deg,#3A3A3A,#8E9A84 55%,#2A2A2A)" role="img" aria-label="Photo of a bartender stirring a cocktail garnished with lime"></div>
  <div class="badge" style="left:652px;top:1094px;width:96px;height:96px;background:var(--teal-bright);font:700 20px 'Roboto',sans-serif;letter-spacing:2px">TWIG</div>
</section>

<!-- collection -->
<section class="abs collection">
  <h2 class="abs display">OUR COLLECTION</h2>
  <div class="card" style="left:107px">
    <div class="shot" style="background:linear-gradient(135deg,#5A4030,#B7833F)" role="img" aria-label="Photo of a jar of dried cocktail mix"></div>
    <div class="stars"><b>★★★★★</b> (201)</div><div class="name">Qui Officia Deserunt Mollit</div>
    <div class="price">$12.99 <s>$20.99</s></div><div class="add">ADD</div>
  </div>
  <div class="card" style="left:357px">
    <div class="shot" style="background:linear-gradient(135deg,#E8E8E8,#A48160)" role="img" aria-label="Photo of a glass jar of dried fruit mix"></div>
    <div class="stars"><b>★★★★★</b> (201)</div><div class="name">Qui Officia Deserunt Mollit</div>
    <div class="price">$12.99 <s>$20.99</s></div><div class="add">ADD</div>
  </div>
  <div class="card" style="left:606px">
    <div class="shot" style="background:linear-gradient(135deg,#F2EEE8,#D98A35)" role="img" aria-label="Photo of dried orange slices in a jar"></div>
    <div class="stars"><b>★★★★★</b> (201)</div><div class="name">Qui Officia Deserunt Mollit</div>
    <div class="price">$12.99 <s>$20.99</s></div><div class="add">ADD</div>
  </div>
  <div class="card" style="left:853px">
    <div class="shot" style="background:linear-gradient(135deg,#F4F2EF,#9C6A3E)" role="img" aria-label="Photo of a wooden bowl of nuts and dried fruit"></div>
    <div class="stars"><b>★★★★★</b> (201)</div><div class="name">Qui Officia Deserunt Mollit</div>
    <div class="price">$12.99 <s>$20.99</s></div><div class="add">ADD</div>
  </div>
  <div class="abs dots"><i></i><i></i><i></i></div>
</section>

<!-- recipes -->
<section class="recipes">
  <div class="ring" style="left:134px;top:1973px;width:420px;height:420px;background:var(--teal-pale)"></div>
  <div class="ring" style="left:148px;top:1987px;width:392px;height:392px;background:var(--teal)"></div>
  <div class="ring" style="left:168px;top:2007px;width:354px;height:354px;background:linear-gradient(160deg,#6B6B6B,#B5563A 55%,#2B2520)" role="img" aria-label="Photo of a bartender garnishing a red cocktail with orange peel"></div>
  <div class="badge" style="left:450px;top:2236px;width:96px;height:96px;background:var(--teal-bright)">
    <svg width="44" height="52" viewBox="0 0 44 52"><path d="M4 8h36L22 28z" fill="none" stroke="#fff" stroke-width="2.6"/><path d="M22 28v18M12 48h20" stroke="#fff" stroke-width="2.6"/><circle cx="13" cy="8" r="5" fill="none" stroke="#fff" stroke-width="2"/></svg>
  </div>
  <h2 class="abs display">RECIPES</h2>
  <p class="abs copy">Eaque Ipsa Quae Ab Illo Inventore Veritatis Et Quasi Architecto Beatae Vitae Dicta Sunt Explicabo. Nemo Enim Ipsam Voluptatem Quia Voluptas Sit Aspernatur Aut Odit Aut Fugit, Sed Quia Consequuntur Magni Dolores Eos Qui Ratione Voluptatem Sequi Nesciunt. Neque Porro Quisquam Est, Qui Dolorem Ipsum Quia Dolor Sit Amet, Consectetur, Adipisci Velit, Sed Quia Non</p>
  <div class="btn-outline" style="left:632px;top:2273px;width:162px;height:47px">LEARN MORE</div>
</section>

<!-- spirits -->
<section class="abs spirits">
  <h2 class="abs display">SHOP TWIG BY SPIRIT</h2>
  <div class="spirit" style="left:116px"><svg width="70" height="90" viewBox="0 0 70 90"><g fill="none" stroke="#00AB8E" stroke-width="2.6"><path d="M16 4h10v16l8 10v54H8V30l8-10z"/><circle cx="21" cy="56" r="8"/><path d="M44 58h20l-3 28H47z"/></g></svg><span>QUIS AUTEM</span></div>
  <div class="spirit" style="left:280px"><svg width="70" height="90" viewBox="0 0 70 90"><g fill="none" stroke="#00AB8E" stroke-width="2.6"><path d="M14 22h40l-5 64H19z"/><path d="M36 22l12-18"/><circle cx="34" cy="54" r="9"/></g></svg><span>QUIS AUTEM</span></div>
  <div class="spirit" style="left:442px"><svg width="70" height="90" viewBox="0 0 70 90"><g fill="none" stroke="#00AB8E" stroke-width="2.6"><path d="M28 4h14v18l10 10v54H18V32l10-10z"/><rect x="22" y="46" width="26" height="24"/><circle cx="35" cy="58" r="5"/></g></svg><span>QUIS AUTEM</span></div>
  <div class="spirit is-active" style="left:605px"><svg width="70" height="90" viewBox="0 0 70 90"><g fill="none" stroke="#00AB8E" stroke-width="2.6"><path d="M29 4h12v20l10 10v52H19V34l10-10z"/><rect x="24" y="48" width="22" height="20"/><path d="M28 14h14"/></g></svg><span>QUIS AUTEM</span></div>
  <div class="spirit" style="left:768px"><svg width="70" height="90" viewBox="0 0 70 90"><g fill="none" stroke="#00AB8E" stroke-width="2.6"><path d="M10 26h50l-4 58H14z"/><rect x="20" y="40" width="14" height="14"/><rect x="36" y="46" width="14" height="14"/><path d="M14 66h42"/></g></svg><span>QUIS AUTEM</span></div>
  <div class="spirit" style="left:932px"><svg width="70" height="90" viewBox="0 0 70 90"><g fill="none" stroke="#00AB8E" stroke-width="2.6"><circle cx="35" cy="12" r="6"/><path d="M28 22h14l8 14H20z"/><rect x="14" y="40" width="42" height="36" rx="4"/><path d="M14 58h42M6 86h58"/></g></svg><span>QUIS AUTEM</span></div>
</section>

<!-- choose -->
<section class="choose">
  <h2 class="abs display">CHOOSE YOUR COCKTAIL</h2>
  <p class="abs copy">Eaque Ipsa Quae Ab Illo Inventore Veritatis Et Quasi Architecto Beatae Vitae Dicta Sunt Explicabo. Nemo Enim Ipsam Voluptatem Quia Voluptas Sit Aspernatur Aut Odit Aut Fugit, Sed Quia Consequuntur Magni Dolores Eos Qui Ratione Voluptatem Sequi Nesciunt. Neque Porro Quisquam Est, Qui Dolorem Ipsum Quia Dolor Sit Amet, Consectetur, Adipisci Velit, Sed Quia Non</p>
  <div class="btn-outline" style="left:115px;top:3171px;width:161px;height:48px">LEARN MORE</div>
  <div class="abs" style="left:676px;top:2934px;width:421px;height:305px;background:var(--teal-soft)"></div>
  <div class="abs" style="left:667px;top:2925px;width:421px;height:305px;background:linear-gradient(135deg,#1C2430,#5A3C6E 50%,#2A2018)" role="img" aria-label="Photo of a bartender pouring a drink behind a lit bar"></div>
  <div class="badge" style="left:624px;top:3021px;width:96px;height:96px;background:var(--teal-bright)">
    <svg width="44" height="52" viewBox="0 0 44 52"><path d="M4 8h36L22 28z" fill="none" stroke="#fff" stroke-width="2.6"/><path d="M22 28v18M12 48h20" stroke="#fff" stroke-width="2.6"/><circle cx="13" cy="8" r="5" fill="none" stroke="#fff" stroke-width="2"/></svg>
  </div>
</section>

<!-- footer -->
<footer class="abs footer">
  <h3 class="abs" style="left:149px;top:56px">SUBSCRIBE TO OUR NEWSLETTER</h3>
  <div class="abs signup"><span>Enter Email Address</span><b>SIGH UP</b></div>
  <div class="abs rule" style="top:146px"></div>
  <div class="abs col" style="left:125px;top:190px"><h4>QUICK LINKS</h4><ul><li>About Us</li><li>Shop</li><li>Gifts</li><li>Recipes</li><li>Merch</li><li>Stockists</li></ul></div>
  <div class="abs col" style="left:361px;top:190px"><h4>INFORMATION</h4><ul><li>Eaque Ipsa Quae</li><li>Ab Illo Inventore</li><li>Veritatis Et Quasi</li><li>Architecto Beatae</li><li>Vitae Dicta Sunt</li><li>Explicabo. Nemo</li></ul></div>
  <div class="abs col" style="left:623px;top:190px"><h4>CONTACT US</h4>
    <div class="contact-row"><svg width="14" height="20" viewBox="0 0 14 20"><path d="M7 0a7 7 0 00-7 7c0 5 7 13 7 13s7-8 7-13a7 7 0 00-7-7z" fill="#fff"/><circle cx="7" cy="7" r="2.6" fill="#00AB8E"/></svg><span>1233Nemo Enim Ipsam<br>Voluptatem Quia</span></div>
    <div class="contact-row"><svg width="16" height="16" viewBox="0 0 16 16"><path d="M3 1l3 3-2 2c1 2 3 4 5 5l2-2 3 3-2 3C7 15 1 9 0 4z" fill="#fff"/></svg><span>(+000) 123 456 789 0</span></div>
    <div class="contact-row"><svg width="18" height="14" viewBox="0 0 18 14"><rect x="1" y="1" width="16" height="12" fill="none" stroke="#fff" stroke-width="1.6"/><path d="M1 1l8 6 8-6" fill="none" stroke="#fff" stroke-width="1.6"/></svg><span>info@twigcraftcocktail.com</span></div>
  </div>
  <div class="abs col" style="left:946px;top:190px"><h4>FOLLOW UP</h4><div class="socials" style="margin-top:14px"><i></i><i></i><i></i><i></i></div></div>
  <div class="abs rule" style="top:414px"></div>
  <div class="abs copyright">© 2021 TWIG Craft Cocktails. , LLC. All rights reserved.</div>
</footer>

</body>
</html>
```